Nut Brittle Box Design for Packaging

I want t box design for my nut brittles, Needs to stand out for high end shops, particularly duty free shops. I want a box design for 3 individual flavours and a box design for gift box inclusive of the 3 flavours. I want something clean but classy, not busy, I have uploaded a pic of the current packaging which I use in local shops but not the packaging needs to be in a box for easy transporting. I have also uploaded the nutritional labelling for each flavour needed as well. I would be good to get a design that incorporates each of the individual flavour ribbon colours.
Updates

Box dimensions W10cm H12cm D3cm

Target Market(s)

Duty free shops and high end gift shops

Requirements
Must have
• Clean and classy
Nice to have
• Interchangeable nutrional info box and brittle flavour name

```html
<!DOCTYPE html>
<html lang="en">
<head>
<meta charset="utf-8">
<title>Swan Coast Brittle – Pistachio &amp; Lemon Myrtle Box Dieline</title>
<link rel="stylesheet" href="https://fonts.googleapis.com/css2?family=Montserrat:ital,wght@0,400;0,500;0,700;1,300&family=Josefin+Sans:wght@400;600&family=Cinzel:wght@700&family=Playfair+Display:wght@600&display=swap">
<style>
  :root {
    --paper: #ffffff;
    --cream: #fcf9f8;
    --teal: #8ecfcf;
    --teal-light: #b6e0df;
    --ink: #111111;
    --text: #4f4f4f;
    --text-soft: #7a7a7a;
    --rule: #555555;
  }
  html, body { margin: 0; padding: 0; width: 1200px; height: 1061px; overflow: hidden; background: var(--paper); }
  .dieline { display: block; width: 1200px; height: 1061px; }
  .cut { fill: none; stroke: var(--ink); stroke-width: 3; stroke-linejoin: round; }
  .fold { fill: none; stroke: var(--ink); stroke-width: 3; stroke-dasharray: 10 6; }
  .panel-cream { fill: var(--cream); }
  .pattern-band { fill: var(--teal); }
  .nutrition-panel { fill: var(--paper); }
  .nf { font-family: "Montserrat", sans-serif; fill: var(--text); }
  .nf-title { font-size: 16px; font-weight: 700; }
  .nf-body { font-size: 11.5px; }
  .nf-bold { font-weight: 700; }
  .nf-small { font-size: 9px; }
  .nf-tiny { font-size: 7px; }
  .nf-rule { stroke: var(--rule); stroke-width: 1.2; }
  .nf-rule-thick { stroke: var(--rule); stroke-width: 4; }
  .story { font-family: "Montserrat", sans-serif; font-size: 9.5px; font-style: italic; font-weight: 300; fill: var(--text-soft); letter-spacing: 0.3px; }
  .facts { font-family: "Montserrat", sans-serif; font-size: 9.5px; fill: var(--text); letter-spacing: 0.5px; }
  .badge { fill: none; stroke: var(--text); stroke-width: 2; }
  .brand-name { font-family: "Josefin Sans", sans-serif; font-size: 21px; font-weight: 400; fill: var(--text); letter-spacing: 3.5px; text-anchor: middle; }
  .label-card { fill: var(--paper); }
  .label-frame { fill: none; stroke: #8a8a8a; stroke-width: 1.5; }
  .flavour-name { font-family: "Cinzel", serif; font-size: 33px; font-weight: 700; fill: #4a4a4a; text-anchor: middle; }
  .flavour-type { font-family: "Montserrat", sans-serif; font-size: 14px; font-weight: 400; fill: var(--text); text-anchor: middle; letter-spacing: 0.5px; }
  .net-weight { font-family: "Playfair Display", serif; font-size: 22px; font-weight: 600; fill: #4a4a4a; text-anchor: middle; }
</style>
</head>
<body>
<svg class="dieline" viewBox="0 0 1690 1494" xmlns="http://www.w3.org/2000/svg">
  <defs>
    <filter id="card-shadow" x="-10%" y="-10%" width="120%" height="120%">
      <feDropShadow dx="2" dy="3" stdDeviation="3" flood-color="#000" flood-opacity="0.25"/>
    </filter>
  </defs>

  <!-- Panels -->
  <g class="panels">
    <rect class="panel-cream" x="252" y="218" width="536" height="190"/>
    <rect class="panel-cream" x="62" y="408" width="1450" height="402"/>
    <g role="img" aria-label="Teal band with a light line-drawn floral pattern">
      <path class="pattern-band" d="M62 810 H1512 V1090 H1532 V1295 H978 V1090 H62 Z"/>
    </g>
  </g>

  <!-- Cut lines -->
  <g class="cut-lines">
    <path class="cut" d="M255 218 V185 Q255 112 330 112 H712 Q787 112 787 185 V218"/>
    <path class="cut" d="M62 408 L72 390 L100 254 H243 V395 L252 408"/>
    <path class="cut" d="M788 408 L795 395 V254 H938 L965 390 L978 408"/>
    <path class="cut" d="M978 408 H1512 L1618 487 V1022 L1512 1090"/>
    <path class="cut" d="M62 408 V1090"/>
    <path class="cut" d="M62 1090 L72 1108 V1245 H215 L240 1108 L252 1090"/>
    <path class="cut" d="M788 1090 L797 1108 L825 1245 H968 V1108 L978 1090"/>
    <path class="cut" d="M978 1090 V1280"/>
    <path class="cut" d="M1512 1090 V1280"/>
    <path class="cut" d="M978 1280 V1318 Q978 1388 1050 1388 H1440 Q1510 1388 1510 1318 V1280"/>
  </g>

  <!-- Fold lines -->
  <g class="fold-lines">
    <line class="fold" x1="255" y1="218" x2="787" y2="218"/>
    <line class="fold" x1="62" y1="408" x2="1512" y2="408"/>
    <line class="fold" x1="62" y1="1090" x2="1512" y2="1090"/>
    <line class="fold" x1="978" y1="1280" x2="1512" y2="1280"/>
    <line class="fold" x1="252" y1="408" x2="252" y2="1090"/>
    <line class="fold" x1="788" y1="408" x2="788" y2="1090"/>
    <line class="fold" x1="978" y1="408" x2="978" y2="1090"/>
    <line class="fold" x1="1512" y1="408" x2="1512" y2="1090"/>
  </g>

  <!-- Back panel: nutrition facts -->
  <g class="nutrition-facts">
    <rect class="nutrition-panel" x="287" y="445" width="254" height="517"/>
    <text class="nf nf-title" x="303" y="479">Nutrition Facts</text>
    <text class="nf nf-body" x="304" y="508">Serving Size</text>
    <text class="nf nf-body" x="520" y="508" text-anchor="end">Box (g)</text>
    <line class="nf-rule-thick" x1="304" y1="517" x2="525" y2="517"/>
    <text class="nf nf-body nf-bold" x="305" y="538">8 Serving per container</text>
    <line class="nf-rule" x1="304" y1="548" x2="525" y2="548"/>
    <text class="nf nf-small" x="305" y="564">Amount per serving</text>
    <text class="nf nf-body nf-bold" x="305" y="586">Calories</text>
    <text class="nf nf-body nf-bold" x="523" y="586" text-anchor="end">125</text>
    <line class="nf-rule-thick" x1="304" y1="594" x2="525" y2="594"/>
    <text class="nf nf-small" x="522" y="609" text-anchor="end">% Daily Value*</text>
    <line class="nf-rule" x1="304" y1="618" x2="525" y2="618"/>

    <g class="nf nf-small">
      <text x="305" y="635" class="nf-bold">Total Fat</text><text x="417" y="635" class="nf-bold">127 mg</text><text x="522" y="635" text-anchor="end" class="nf-bold">0.4%</text>
      <line class="nf-rule" x1="304" y1="644" x2="525" y2="644"/>
      <text x="323" y="661">Saturates</text><text x="417" y="661">12 mg</text><text x="520" y="661" text-anchor="end" class="nf-bold">58.2%</text>
      <line class="nf-rule" x1="304" y1="669" x2="525" y2="669"/>
      <text x="323" y="686">Salt</text><text x="417" y="686">81 mg</text><text x="520" y="686" text-anchor="end" class="nf-bold">15.5%</text>
      <line class="nf-rule" x1="304" y1="694" x2="525" y2="694"/>
      <text x="323" y="711">Trans flat</text><text x="417" y="711">69 mg</text><text x="518" y="711" text-anchor="end" class="nf-bold">1.5%</text>
      <line class="nf-rule" x1="304" y1="719" x2="525" y2="719"/>
      <text x="323" y="736" class="nf-bold">Sodium</text><text x="417" y="736" class="nf-bold">324 mg</text><text x="520" y="736" text-anchor="end" class="nf-bold">5.4%</text>
      <line class="nf-rule" x1="304" y1="744" x2="525" y2="744"/>
      <text x="323" y="761" class="nf-bold">Protein</text><text x="417" y="761" class="nf-bold">20 mg</text><text x="518" y="761" text-anchor="end" class="nf-bold">6.12%</text>
      <line class="nf-rule" x1="304" y1="769" x2="525" y2="769"/>
      <text x="323" y="786" class="nf-bold">Cholesterol</text><text x="417" y="786" class="nf-bold">11 mg</text><text x="514" y="786" text-anchor="end" class="nf-bold">5.6%</text>
      <line class="nf-rule" x1="304" y1="795" x2="525" y2="795"/>
      <text x="305" y="812" class="nf-bold">Protein 0g</text><text x="417" y="812" class="nf-bold">25 mg</text><text x="518" y="812" text-anchor="end" class="nf-bold">4 .3%</text>
    </g>
    <line class="nf-rule-thick" x1="304" y1="820" x2="525" y2="820"/>
    <text class="nf nf-tiny nf-bold" x="418" y="838">Calories:</text>
    <line class="nf-rule" x1="304" y1="843" x2="525" y2="843"/>
    <g class="nf nf-tiny">
      <text x="308" y="855" class="nf-bold">Total Fat</text><text x="417" y="855">Less than</text>
      <text x="308" y="865" class="nf-bold">Sat Fat</text><text x="417" y="865">Less than</text>
      <text x="308" y="875" class="nf-bold">Cholesterol</text><text x="417" y="875">Less than</text>
      <text x="308" y="885" class="nf-bold">Sodium</text><text x="417" y="885">Less than</text>
      <text x="308" y="895" class="nf-bold">Total carbohydrate</text>
      <text x="304" y="920"><tspan class="nf-bold">Percent daily values</tspan> are based on a 2,000 calorie</text>
      <text x="304" y="930">diet. Your own daily values may be higher</text>
      <text x="304" y="940">or lower depending on needs.</text>
    </g>
  </g>

  <!-- Back panel: product story and ingredients -->
  <g class="product-copy">
    <text class="story">
      <tspan x="563" y="454">Indulge in the old-fashioned goodness</tspan>
      <tspan x="563" y="466">of a Nut Brittle made with freshly</tspan>
      <tspan x="563" y="478">roasted gourmet nuts. This crispy</tspan>
      <tspan x="563" y="490">treat is handmade using traditional</tspan>
      <tspan x="563" y="502">methods to create the perfect</tspan>
      <tspan x="563" y="514">balance of sweetness and nuttiness.</tspan>
      <tspan x="563" y="526">Enjoy each crunchy bite and savor</tspan>
      <tspan x="563" y="538">the nostalgic flavor of this classic</tspan>
      <tspan x="563" y="550">candy.</tspan>
    </text>
    <text class="facts">
      <tspan x="563" y="574">Ingredients: Sugar, Corn Syrup,</tspan>
      <tspan x="563" y="586">Peanuts, Almonds, Hasel Nuts,</tspan>
      <tspan x="563" y="598">Pistachio, Baking Soda, Salt.</tspan>
      <tspan x="563" y="610">No Additives. No Preservatives.</tspan>
      <tspan x="563" y="634">Gluten free. Contains Nuts.</tspan>
      <tspan x="563" y="646">Manufactured on equipment that</tspan>
      <tspan x="563" y="658">also processes milk, soy, tree nuts</tspan>
      <tspan x="563" y="670">and eggs.</tspan>
    </text>
    <g class="dietary-badges">
      <circle class="badge" cx="601" cy="751" r="37"/>
      <circle class="badge" cx="601" cy="751" r="24"/>
      <circle class="badge" cx="705" cy="751" r="37"/>
      <circle class="badge" cx="705" cy="751" r="24"/>
    </g>
  </g>

  <!-- Front panel -->
  <g class="front-panel">
    <g class="dietary-badges">
      <circle class="badge" cx="1047" cy="477" r="37"/>
      <circle class="badge" cx="1047" cy="477" r="24"/>
      <circle class="badge" cx="1047" cy="575" r="37"/>
      <circle class="badge" cx="1047" cy="575" r="24"/>
    </g>
    <text class="brand-name" x="1247" y="604">SWAN COAST</text>
    <text class="brand-name" x="1247" y="634">BRITTLE</text>

    <g class="flavour-label">
      <rect class="label-card" x="1093" y="657" width="305" height="305" filter="url(#card-shadow)"/>
      <rect class="label-frame" x="1096" y="660" width="299" height="299"/>
      <rect class="label-frame" x="1101" y="665" width="289" height="289"/>
      <text class="flavour-name" x="1245" y="759">Pistachio &amp;</text>
      <text class="flavour-name" x="1245" y="800">Lemon Myrtle</text>
      <text class="flavour-type" x="1245" y="844">ARTISANAL NUT BRITTLE</text>
      <text class="net-weight" x="1245" y="925">120g</text>
    </g>
  </g>
</svg>
</body>
</html>
```